Australian Meat, Seafood and Fresh Produce Website

Our organization is looking to design a simple, but eye catching website to show our services.
Our company exports West Australian FRESH fruit and vegetables, seafood and meat.
The website we are looking for would consist of:
- Landing Page
- Company info
- Directors bio
- Page that highlights our products
- Contact us page
We would like it to have a Chinese translated version as well.
Tobin
Target Market(s)
Chinese Market
Industry/Entity Type
It Company
Number of Pages Required
1 page
Look and feel
Each slider illustrates characteristics of the customer's brand and the style your logo design should communicate.

```html
<!DOCTYPE html>
<html lang="en">
<head>
<meta charset="utf-8">
<title>Westgrove Fresh Exports</title>
<link rel="stylesheet" href="https://fonts.googleapis.com/css2?family=PT+Sans:ital,wght@0,400;0,700;1,400&family=EB+Garamond:ital@1&display=swap">
<style>
  :root {
    --forest: #3b4614;
    --forest-deep: #2f3a10;
    --olive-accent: #a7b32a;
    --ink: #1f1f1f;
    --body-ink: #3a3a3a;
    --paper: #ffffff;
    --pill: #e9e9e9;
    --footer: #cfd1c8;
    --bamboo-dark: #1f5a14;
    --bamboo-light: #9fc98a;
    --fruit-orange: #f2a23a;
    --fruit-green: #b9d77a;
  }
  * { box-sizing: border-box; margin: 0; padding: 0; }
  html, body { width: 1200px; height: 960px; overflow: hidden; }
  body {
    position: relative;
    font-family: "PT Sans", sans-serif;
    color: var(--ink);
    background: linear-gradient(90deg, var(--bamboo-dark) 0%, #3e8a2a 6%, #2a6a1a 12%, #4f8f3c 100%);
  }
  .backdrop-right {
    position: absolute; left: 1051px; top: 0; width: 149px; height: 960px;
    background: linear-gradient(180deg, #e8f2e4 0%, var(--bamboo-light) 35%, #4f9640 70%, #2f6a22 100%);
  }
  .backdrop-left {
    position: absolute; left: 0; top: 0; width: 152px; height: 960px;
    background: linear-gradient(90deg, #2f7a20 0%, #1e5a12 40%, #5fa54a 80%, #9fcf86 100%);
  }
  .page {
    position: absolute; left: 152px; top: 0; width: 899px; height: 960px;
    background: var(--paper);
  }
  .site-header { position: absolute; left: 0; top: 0; width: 899px; height: 187px; }
  .brand-name {
    position: absolute; left: 43px; top: 34px;
    font-size: 52px; font-weight: 400; color: var(--forest); letter-spacing: -1px;
    white-space: nowrap;
  }
  .tagline {
    position: absolute; left: 51px; top: 102px;
    font-family: "EB Garamond", serif; font-style: italic;
    font-size: 27px; color: #8a8a8a;
  }
  .header-produce {
    position: absolute; left: 598px; top: 0; width: 300px; height: 187px;
    background: radial-gradient(ellipse at 50% 50%, var(--fruit-orange) 0%, #f7c978 40%, var(--fruit-green) 62%, rgba(255,255,255,0) 75%);
  }
  .main-nav {
    position: absolute; left: 0; top: 187px; width: 899px; height: 56px;
    background: var(--forest);
    border-bottom: 12px solid #000; height: 68px;
  }
  .main-nav a {
    position: absolute; top: 20px;
    color: #fff; text-decoration: none; font-size: 20px;
  }
  .page-title {
    position: absolute; left: 20px; top: 274px;
    font-size: 25px; font-weight: 400; color: var(--ink);
  }
  .title-rule {
    position: absolute; left: 20px; top: 327px; width: 857px; height: 1px; background: #222;
  }
  .product-card { position: absolute; top: 358px; width: 190px; }
  .product-photo { width: 188px; height: 141px; }
  .product-card h3 { font-size: 15px; font-weight: 700; margin-top: 8px; }
  .product-card p { font-size: 10.5px; line-height: 14px; color: var(--body-ink); margin-top: 6px; }
  .photo-fruit-a { background: linear-gradient(160deg, #3a3226 0%, #c9b66a 45%, #d65a3a 70%, #eee 100%); }
  .photo-fruit-b { background: linear-gradient(160deg, #5a5048 0%, #e4a63a 40%, #c74a3a 65%, #dfe6c0 100%); }
  .photo-fish { background: linear-gradient(180deg, #3e5a2a 0%, #9fb4c4 40%, #5a7a90 60%, #3e5a2a 100%); }
  .photo-grill { background: linear-gradient(160deg, #d04030 0%, #8a3a20 40%, #b8502a 70%, #f2f2f2 100%); }
  .feature-panel {
    position: absolute; left: 24px; top: 638px; width: 846px; height: 253px;
    background: var(--forest); border-radius: 10px; color: #fff;
  }
  .welcome-title {
    position: absolute; left: 34px; top: 26px; font-size: 26px; font-weight: 700; letter-spacing: -0.5px;
  }
  .welcome-photo {
    position: absolute; left: 34px; top: 68px; width: 121px; height: 156px;
    background: linear-gradient(160deg, #7a6a5a 0%, #e4a63a 40%, #c74a3a 62%, #cfe0a8 100%);
  }
  .welcome-text {
    position: absolute; left: 163px; top: 68px; width: 420px;
    font-size: 12.5px; line-height: 15.7px; letter-spacing: -0.2px;
  }
  .read-more {
    position: absolute; font-size: 15px; font-weight: 700; color: var(--olive-accent); text-decoration: none;
  }
  .news-pill {
    position: absolute; left: 596px; top: 22px; width: 219px; height: 37px;
    background: var(--pill); border-radius: 6px;
    color: var(--forest); font-size: 25px; font-weight: 700; text-align: center; line-height: 37px;
    letter-spacing: -0.5px;
  }
  .news-title {
    position: absolute; left: 601px; top: 68px; font-size: 21px; color: var(--olive-accent); font-weight: 400;
  }
  .news-text {
    position: absolute; left: 600px; top: 104px; width: 240px;
    font-size: 12.5px; line-height: 16px; letter-spacing: -0.2px;
  }
  .site-footer {
    position: absolute; left: -2px; top: 909px; width: 901px; height: 51px; background: var(--footer);
  }
</style>
</head>
<body>
  <div class="backdrop-left" role="img" aria-label="Blurred green bamboo stalks"></div>
  <div class="backdrop-right" role="img" aria-label="Blurred green bamboo leaves in soft light"></div>

  <div class="page">
    <header class="site-header">
      <div class="brand-name">Westgrove Fresh Exports</div>
      <div class="tagline">Tag Line here</div>
      <div class="header-produce" role="img" aria-label="Diced mango, cheese and celery with chives"></div>
    </header>

    <nav class="main-nav">
      <a href="#" style="left:17px">Home</a>
      <a href="#" style="left:114px">About Us</a>
      <a href="#" style="left:230px">Directors</a>
      <a href="#" style="left:338px">Our Products</a>
      <a href="#" style="left:477px">Contact Us</a>
    </nav>

    <h1 class="page-title">Lorem Ipsum dummy text</h1>
    <div class="title-rule"></div>

    <article class="product-card" style="left:20px">
      <div class="product-photo photo-fruit-a" role="img" aria-label="Platter of sliced fruit with strawberries"></div>
      <h3>Title 1</h3>
      <p>Lorem Ipsum is simply dummy text of the .printing and typesetting industry Lorem Ipsum has been the industry's standard dummy text ever since the 1500</p>
    </article>
    <article class="product-card" style="left:249px">
      <div class="product-photo photo-fruit-b" role="img" aria-label="Fresh fruit platter with mango and berries"></div>
      <h3>Title 1</h3>
      <p>Lorem Ipsum is simply dummy text of the .printing and typesetting industry Lorem Ipsum has been the industry's standard dummy text ever since the 1500</p>
    </article>
    <article class="product-card" style="left:471px">
      <div class="product-photo photo-fish" role="img" aria-label="Three fresh sardines on green leaves"></div>
      <h3>Title 1</h3>
      <p>Lorem Ipsum is simply dummy text of the .printing and typesetting industry Lorem Ipsum has been the industry's standard dummy text ever since the 1500</p>
    </article>
    <article class="product-card" style="left:690px">
      <div class="product-photo photo-grill" role="img" aria-label="Grilled sausages and meat skewers with vegetables"></div>
      <h3>Title 1</h3>
      <p>Lorem Ipsum is simply dummy text of the .printing and typesetting industry Lorem Ipsum has been the industry's standard dummy text ever since the 1500</p>
    </article>

    <section class="feature-panel">
      <h2 class="welcome-title">Welcome to our Website</h2>
      <div class="welcome-photo" role="img" aria-label="Fruit platter with mango and melon"></div>
      <p class="welcome-text">.Lorem Ipsum is simply dummy text of the printing and typesetting industry ,Lorem Ipsum has been the industry's standard dummy text ever since the 1500s when an unknown printer took a galley of type and scrambled it to make a type specimen book. It has survived not only five centuries, but also the leap into electronic typesetting, remaining essentially unchanged. It was popularised in the 1960s with the release of Letraset sheets containing Lorem Ipsum passages</p>
      <a class="read-more" href="#" style="left:166px; top:183px">...Read More</a>

      <div class="news-pill">Whats New</div>
      <h3 class="news-title">Title goes here</h3>
      <p class="news-text">Lorem Ipsum is simply dummy textof the print and typesetting industry.. Lorem Ipsum has been .the industry's standard dummy text ever since</p>
      <a class="read-more" href="#" style="left:602px; top:171px">...Read More</a>
    </section>

    <footer class="site-footer"></footer>
  </div>
</body>
</html>
```